International Fundraising Consultancy needs a new PowerPoint Design

We train international nonprofits on how to fundraise globally. We plan to keep our current logo design and color, as we love the color orange, but want a cleaner, fresher, less cluttered template for our PowerPoint presentations. The finished product needs to be easy to edit, and include template slides that can feature tables, graphics and images. We would like a color scheme for graphics.The layout should be lighter, clear, attractive and easy to read and understand. We also want to use the same template for webinar slides. We have attached an example of our current PowerPoint template with identifying client information removed. The green slide that looks like a clapperboard fro a film is basically just a placeholder that indicates a break for an interactive exercise.

Target Market(s)

Board members, staff members, museum executives, leadership of NGOs, top businesspeople in Europe, many with a modern sense of aesthetics in the art world

Industry/Entity Type

Cleaner

Font styles to use
Sans Serif

Colors
f78f20
f37022

Requirements
Must have
• Orange colors, keep our Vormkelingen logo
• Good templates for tables, photos and graphics

```html
<!DOCTYPE html>
<html lang="en">
<head>
<meta charset="utf-8">
<title>Fundraising Board Workshop – Slide Overview</title>
<link href="https://fonts.googleapis.com/css2?family=Oswald:wght@400;500&family=Open+Sans:wght@400;600&display=swap" rel="stylesheet">
<style>
:root{
  --sorter-bg:#b4b7bd;
  --sorter-bg-dark:#9ea2a9;
  --slide-bg:#f3f0ea;
  --orange:#f37022;
  --orange-light:#f78f20;
  --orange-pale:#fbc79a;
  --peach:#fbd5bd;
  --grey-text:#7b7b7b;
  --grey-wedge:#d9d7d3;
  --dark:#2b2b2b;
  --number:#4a4d52;
}
*{box-sizing:border-box;margin:0;padding:0}
html,body{width:1200px;height:513px;overflow:hidden}
body{background:linear-gradient(180deg,var(--sorter-bg),var(--sorter-bg-dark));font-family:"Open Sans",sans-serif;position:relative}
.slide{position:absolute;width:225px;height:157px;background:var(--slide-bg);overflow:hidden;box-shadow:0 1px 3px rgba(0,0,0,.35)}
.slide::before{content:"";position:absolute;inset:0;background:var(--grey-wedge);clip-path:polygon(96% 6%,100% 3%,100% 86%,84% 91%);opacity:.8}
.slide::after{content:"";position:absolute;inset:0;background:linear-gradient(90deg,var(--orange-light),var(--orange-pale) 30%,var(--orange-light));clip-path:polygon(0 93%,100% 84%,100% 100%,0 100%)}
.slide.is-selected{outline:3px solid var(--orange-light);outline-offset:0}
.slide-number{position:absolute;font-size:9px;color:var(--number)}
.brand{position:absolute;left:6px;bottom:8px;display:flex;align-items:center;gap:3px;font-size:4.6px;color:var(--orange);z-index:2}
.brand-dot{width:8px;height:8px;background:var(--dark);border-radius:50%}
.title-dots{position:absolute;right:16px;top:15px;display:flex;align-items:center;gap:2px;z-index:2}
.title-dots span{display:block;border-radius:50%;background:var(--orange-light)}
.title-dots span:nth-child(1){width:2px;height:2px;opacity:.5}
.title-dots span:nth-child(2){width:2px;height:2px;opacity:.7}
.title-dots span:nth-child(3){width:3px;height:3px}
.title-dots span:nth-child(4){width:4px;height:4px}
.slide-title{position:absolute;left:18px;top:10px;font-family:"Oswald",sans-serif;font-weight:400;color:var(--orange-light);font-size:13px;letter-spacing:.2px;z-index:2;white-space:nowrap}
.slide-title.small{font-size:8.5px;top:13px}
.body-text{position:absolute;left:18px;font-size:5.6px;line-height:1.35;color:var(--grey-text);z-index:2}
.body-text .accent{color:var(--orange)}
.art{position:absolute;z-index:1}
.cover-title{position:absolute;left:20px;top:50px;font-family:"Oswald",sans-serif;font-size:8.5px;letter-spacing:2.4px;color:var(--orange-light)}
.cover-sub{position:absolute;left:20px;top:66px;font-size:4.6px;color:var(--grey-text)}
.cover-date{position:absolute;left:20px;top:82px;font-size:4.4px;letter-spacing:6.5px;color:var(--orange-light)}
.agenda-title{position:absolute;left:30px;top:12px;font-family:"Oswald",sans-serif;font-size:11px;letter-spacing:5px;color:var(--orange-light)}
.agenda{position:absolute;left:30px;top:40px;width:170px;list-style:none;z-index:2}
.agenda li{display:flex;align-items:center;font-size:4.3px;color:var(--grey-text);height:11.2px}
.agenda li::after{content:"";flex:1;border-bottom:1px dotted #c5c1b9;margin:0 3px}
.agenda li i{order:2;display:block;width:6px;height:6px;border:1.4px solid var(--grey-wedge);border-radius:50%}
.bubble{position:absolute;background:linear-gradient(180deg,var(--orange-pale),var(--orange-light));border-radius:6px;font-size:5px;color:#7a4a25;padding:6px;z-index:2}
.caption{position:absolute;left:0;right:0;text-align:center;font-size:5.2px;color:var(--grey-text);z-index:2}
.source-tag{position:absolute;right:8px;bottom:14px;background:var(--orange-pale);color:#8a5a35;font-size:3.8px;padding:2px 8px;z-index:3}
.checklist{position:absolute;left:36px;top:56px;list-style:none;font-size:5.6px;color:var(--grey-text);z-index:2}
.checklist li{display:flex;align-items:center;gap:6px;height:9px}
.checklist li::before{content:"";width:4px;height:4px;border:.8px solid var(--dark)}
</style>
</head>
<body>

<!-- Row 1 -->
<section class="slide" style="left:15px;top:8px">
  <div class="cover-title">FUNDRAISING BOARD WORKSHOP</div>
  <div class="cover-sub">Anneke Vormkelingen, CFRE , Principal , Vormkelingen &amp; Associates</div>
  <div class="cover-date">SEPTEMBER 19, 2014</div>
  <div class="brand"><span class="brand-dot"></span>Vormkelingen &amp; Associates</div>
</section>
<div class="slide-number" style="left:15px;top:182px">1</div>

<section class="slide" style="left:254px;top:8px">
  <div class="agenda-title">AGENDA</div>
  <ul class="agenda">
    <li>•Introduction<i></i></li>
    <li>•Philanthropy's vital role for the Museum<i></i></li>
    <li>•Role of the Fundraising Board<i></i></li>
    <li>•Cultivation strategies<i></i></li>
    <li>•Solicitation strategies<i></i></li>
    <li>•Stewardship<i></i></li>
    <li>•Next steps<i></i></li>
  </ul>
  <div class="brand"><span class="brand-dot"></span>Vormkelingen &amp; Associates</div>
</section>
<div class="slide-number" style="left:254px;top:182px">2</div>

<section class="slide" style="left:494px;top:8px">
  <h2 class="slide-title">WHO IS WHO?</h2>
  <div class="title-dots"><span></span><span></span><span></span><span></span></div>
  <div class="art" role="img" aria-label="Cartoon clapperboard character on an orange shape, marking an interactive break" style="left:45px;top:30px;width:130px;height:108px;background:radial-gradient(ellipse at 40% 55%,var(--orange-light) 0 45%,transparent 46%),linear-gradient(160deg,#1d1d1d,#3a3a3a);background-blend-mode:normal;border-radius:40% 50% 45% 55%"></div>
  <div class="brand"><span class="brand-dot"></span>Vormkelingen &amp; Associates</div>
</section>
<div class="slide-number" style="left:494px;top:182px">3</div>

<section class="slide" style="left:733px;top:8px">
  <h2 class="slide-title small">PHILANTHROPY IS ENABLING YOUR DONORS' DREAMS</h2>
  <div class="title-dots"><span></span><span></span><span></span><span></span></div>
  <div class="art" role="img" aria-label="Photograph of a crowd on stone steps above a banner at a historic march" style="left:15px;top:32px;width:155px;height:110px;background:linear-gradient(180deg,#d9d3c8 0%,#8f7f6e 45%,#3a3b52 75%,#1f2238 100%)"></div>
  <div class="brand"><span class="brand-dot"></span>Vormkelingen &amp; Associates</div>
</section>
<div class="slide-number" style="left:733px;top:182px">4</div>

<section class="slide" style="left:973px;top:8px">
  <h2 class="slide-title">WHY DO YOU GIVE?</h2>
  <div class="title-dots"><span></span><span></span><span></span><span></span></div>
  <div class="art" role="img" aria-label="Cartoon clapperboard character on an orange shape, marking an interactive break" style="left:45px;top:30px;width:130px;height:108px;background:radial-gradient(ellipse at 40% 55%,var(--orange-light) 0 45%,transparent 46%),linear-gradient(160deg,#1d1d1d,#3a3a3a);border-radius:40% 50% 45% 55%"></div>
  <div class="brand"><span class="brand-dot"></span>Vormkelingen &amp; Associates</div>
</section>
<div class="slide-number" style="left:973px;top:182px">5</div>

<!-- Row 2 -->
<section class="slide is-selected" style="left:15px;top:210px">
  <h2 class="slide-title">WHY?</h2>
  <div class="title-dots"><span></span><span></span><span></span><span></span></div>
  <div class="bubble" style="left:115px;top:32px;width:80px;height:30px">Why did you choose to be involved or join?</div>
  <div class="bubble" style="left:18px;top:66px;width:78px;height:36px">Why do major donors give?</div>
  <div class="brand"><span class="brand-dot"></span>Vormkelingen &amp; Associates</div>
</section>
<div class="slide-number" style="left:15px;top:384px">6</div>

<section class="slide" style="left:254px;top:210px">
  <h2 class="slide-title small">PEOPLE GIVE TO PEOPLE WHO GIVE THEMSELVES!</h2>
  <div class="title-dots"><span></span><span></span><span></span><span></span></div>
  <div class="art" role="img" aria-label="Illustration of two heads facing each other in orange tones" style="left:62px;top:30px;width:100px;height:55px;background:linear-gradient(90deg,#c9661e,#e38a3c 45%,#f3c59a 50%,#e38a3c 55%,#c9661e)"></div>
  <svg class="art" width="225" height="157" viewBox="0 0 225 157" style="left:0;top:0">
    <path d="M40 90 Q30 125 75 128" fill="none" stroke="var(--peach)" stroke-width="7"/>
    <path d="M68 122 L80 128 L68 134 Z" fill="var(--peach)"/>
    <path d="M185 90 Q195 125 150 128" fill="none" stroke="var(--peach)" stroke-width="7"/>
    <path d="M157 122 L145 128 L157 134 Z" fill="var(--peach)"/>
  </svg>
  <div class="caption" style="top:106px">Build meaningful and value-based relationships<br>Connecting to mind &amp; soul</div>
  <div class="brand"><span class="brand-dot"></span>Vormkelingen &amp; Associates</div>
</section>
<div class="slide-number" style="left:254px;top:384px">7</div>

<section class="slide" style="left:494px;top:210px">
  <h2 class="slide-title">WHO GIVES IN THE US?</h2>
  <div class="title-dots"><span></span><span></span><span></span><span></span></div>
  <p class="body-text" style="top:30px">In 2013, American donors gave EUR 258 billion.<br>About 5% (EUR13 billion) goes to arts, culture &amp; humanities.</p>
  <svg class="art" width="225" height="157" viewBox="0 0 225 157" style="left:0;top:0">
    <circle cx="100" cy="107" r="33" fill="var(--peach)"/>
    <path d="M100 107 L100 74 A33 33 0 0 1 110.2 75.6 Z" fill="#c2783f"/>
    <path d="M100 107 L110.2 75.6 A33 33 0 0 1 131.4 97 Z" fill="var(--orange-light)"/>
    <text x="112" y="72" font-size="4.6" fill="#8a8a8a" font-family="Open Sans, sans-serif">Corporations,</text>
    <text x="122" y="78" font-size="4.6" fill="#8a8a8a" font-family="Open Sans, sans-serif">5%</text>
    <text x="136" y="84" font-size="4.6" fill="#8a8a8a" font-family="Open Sans, sans-serif">Foundations,</text>
    <text x="136" y="90" font-size="4.6" fill="#8a8a8a" font-family="Open Sans, sans-serif">14%</text>
    <text x="136" y="136" font-size="4.6" fill="#8a8a8a" font-family="Open Sans, sans-serif">Individuals,</text>
    <text x="136" y="142" font-size="4.6" fill="#8a8a8a" font-family="Open Sans, sans-serif">81%</text>
  </svg>
  <div class="source-tag">Source: Giving Survey 2014</div>
  <div class="brand"><span class="brand-dot"></span>Vormkelingen &amp; Associates</div>
</section>
<div class="slide-number" style="left:494px;top:384px">8</div>

<section class="slide" style="left:733px;top:210px">
  <h2 class="slide-title">WHO GIVES IN THE UK?</h2>
  <div class="title-dots"><span></span><span></span><span></span><span></span></div>
  <p class="body-text" style="top:34px;font-size:6px">In 2011/2012, EUR 3.8 billion was invested in the Arts in<br>England by three sources:</p>
  <p class="body-text" style="top:58px;font-size:6px;line-height:1.55">
    <span class="accent"><i>1.&nbsp; Government funding:</i></span> 41%<br>
    <span class="accent">2.&nbsp; Earned income:</span> 37%<br>
    <span class="accent">3.&nbsp; Private investment:</span> 22%<br>
    &nbsp;&nbsp;&nbsp;&nbsp;• Individual giving: EUR 470 million<br>
    &nbsp;&nbsp;&nbsp;&nbsp;• Trust &amp; Foundation: EUR 219 million<br>
    &nbsp;&nbsp;&nbsp;&nbsp;• Business Investment: EUR 143 million
  </p>
  <div class="brand"><span class="brand-dot"></span>Vormkelingen &amp; Associates</div>
</section>
<div class="slide-number" style="left:733px;top:384px">9</div>

<section class="slide" style="left:973px;top:210px">
  <h2 class="slide-title">WHO GIVES IN THE NL?</h2>
  <div class="title-dots"><span></span><span></span><span></span><span></span></div>
  <p class="body-text" style="top:32px;font-size:5.8px">
    In 2011, EUR 4.3 billion "goede doelen" investments:<br>
    <span class="accent">Individuals:</span> 43% + Bequests/Wills: 6%<br>
    <span class="accent">Corporations:</span> 32%<br>
    <span class="accent">Foundations:</span>7%<br>
    <span class="accent">Lottery:</span> 12%<br>
    <span class="accent">Earned income:</span> xx%<br><br>
    In 2011, EUR 282 million (7%) to arts/culture:<br>
    <span class="accent">Individuals:</span> 26 million + Bequests/Wills: 6 million<br>
    <span class="accent">Corporations:</span> 124 million<br>
    <span class="accent">Foundations:</span>69 million<br>
    <span class="accent">Lottery:</span>62 million
  </p>
  <div class="brand"><span class="brand-dot"></span>Vormkelingen &amp; Associates</div>
</section>
<div class="slide-number" style="left:973px;top:384px">10</div>

<!-- Row 3 -->
<section class="slide" style="left:15px;top:411px">
  <h2 class="slide-title">YOUR ROLE – YOUR CHARTER</h2>
  <div class="title-dots"><span></span><span></span><span></span><span></span></div>
  <div class="art" role="img" aria-label="Photograph of an old handwritten parchment charter" style="left:18px;top:32px;width:150px;height:110px;background:linear-gradient(135deg,#cdbfa6,#a8987c 60%,#8f8068)"></div>
</section>

<section class="slide" style="left:254px;top:411px">
  <h2 class="slide-title small">EXPANDING YOUR MUSEUM'S NETWORK</h2>
  <div class="title-dots"><span></span><span></span><span></span><span></span></div>
  <svg class="art" width="225" height="157" viewBox="0 0 225 157" style="left:0;top:0">
    <g fill="none" stroke="#d9d5ce" stroke-width="1">
      <circle cx="108" cy="105" r="70"/><circle cx="108" cy="105" r="58"/>
      <circle cx="108" cy="105" r="47"/><circle cx="108" cy="105" r="36"/>
      <circle cx="108" cy="105" r="25"/>
      <line x1="108" y1="80" x2="108" y2="35"/><line x1="86" y1="117" x2="47" y2="140"/><line x1="130" y1="117" x2="169" y2="140"/>
    </g>
    <g font-family="Open Sans, sans-serif" font-size="4.4" fill="var(--orange)" text-anchor="middle">
      <text x="108" y="42">The Organization's Universe</text>
      <text x="108" y="53">People With Similar Interests</text>
      <text x="108" y="64">Former Participants</text>
      <text x="108" y="75">Others</text>
      <text x="72" y="96" transform="rotate(-60 72 96)">Board Members</text>
      <text x="145" y="96" transform="rotate(60 145 96)">Volunteers</text>
      <text x="92" y="95">Clients</text>
      <text x="125" y="95">Staff</text>
    </g>
  </svg>
</section>

<section class="slide" style="left:494px;top:411px">
  <h2 class="slide-title small">WHEN IS SOMEONE READY TO BE ASKED?</h2>
  <div class="title-dots"><span></span><span></span><span></span><span></span></div>
  <ul class="checklist" style="top:52px">
    <li>Education</li><li>Involvement</li><li>Cultivation</li><li>Inclination</li><li>Assets</li>
  </ul>
</section>

<section class="slide" style="left:733px;top:411px">
  <h2 class="slide-title small">FOCUS ON CULTIVATING THE "CRITICAL FEW"</h2>
  <div class="title-dots"><span></span><span></span><span></span><span></span></div>
  <div class="art" role="img" aria-label="Sepia photograph of a dartboard close up" style="left:18px;top:32px;width:150px;height:110px;background:radial-gradient(circle at 55% 70%,#b9956a 0 18%,#6e5034 30%,#3a2a1c 55%,#211810)"></div>
</section>

<section class="slide" style="left:973px;top:411px">
  <h2 class="slide-title small">GIVING INCREASES WITH INVOLVEMENT</h2>
  <div class="title-dots"><span></span><span></span><span></span><span></span></div>
  <svg class="art" width="225" height="157" viewBox="0 0 225 157" style="left:0;top:0">
    <line x1="30" y1="38" x2="30" y2="150" stroke="var(--orange-light)" stroke-width="1"/>
    <path d="M110 150 Q125 120 132 95 Q140 65 170 50" fill="none" stroke="var(--orange-light)" stroke-width="1"/>
    <g font-family="Open Sans, sans-serif" font-size="3.8" fill="var(--orange)">
      <text x="16" y="43">High</text>
      <text x="13" y="91">Giving</text>
      <text x="160" y="55">Lead</text>
      <text x="140" y="82">Taking Personal</text>
      <text x="140" y="87">Responsibility</text>
      <text x="128" y="112">Connecting</text>
    </g>
  </svg>
</section>

</body>
</html>
```